Business Card For Kelmora Financial Consulting

Hi, I would like a business card designed. Bold, modern.
Please use the same design as the logo. I have also attached the website design to see the overall theme.
Wordmark Font
Color: Hex: #01AEF7

```html
<!DOCTYPE html>
<html lang="en">
<head>
<meta charset="utf-8">
<title>Kelmora Financial Consulting – Business Card</title>
<link rel="stylesheet" href="https://fonts.googleapis.com/css2?family=Open+Sans:wght@400;700&display=swap">
<style>
  :root {
    --navy: #0a3f67;
    --navy-back: #06436b;
    --sky: #2ca3df;
    --white: #ffffff;
    --backdrop: #dcdcdc;
  }
  * { margin: 0; padding: 0; box-sizing: border-box; }
  html, body { width: 1200px; height: 896px; overflow: hidden; }
  body {
    background: var(--backdrop);
    font-family: "Open Sans", Arial, sans-serif;
    position: relative;
  }
  .card {
    position: absolute;
    left: 334px;
    width: 527px;
    height: 300px;
    overflow: hidden;
  }
  .card--front { top: 126px; background: var(--white); }
  .card--back { top: 474px; background: var(--navy-back); }

  .front__panel {
    position: absolute;
    left: 0; right: 0; bottom: 0;
    top: 124px;
    background: var(--navy);
    border-top: 4px solid var(--sky);
  }

  .brand {
    position: absolute;
    display: flex;
    align-items: center;
  }
  .brand__square {
    border: 3px solid var(--sky);
    flex: none;
  }
  .brand__name {
    font-weight: 700;
    line-height: 1;
    text-transform: uppercase;
  }
  .brand__name span { display: block; }
  .brand__line-main { letter-spacing: 0.12em; }
  .brand__line-sub { color: var(--sky); font-weight: 400; }

  .card--front .brand { top: 22px; right: 21px; gap: 11px; }
  .card--front .brand__square { width: 47px; height: 47px; }
  .card--front .brand__name { color: var(--navy); }
  .card--front .brand__line-main { font-size: 36px; }
  .card--front .brand__line-sub { font-size: 11px; margin-top: 5px; letter-spacing: 1.45em; }

  .card--back .brand { top: 114px; left: 41px; gap: 17px; }
  .card--back .brand__square { width: 72px; height: 72px; border-width: 4px; }
  .card--back .brand__name { color: var(--white); }
  .card--back .brand__line-main { font-size: 54px; }
  .card--back .brand__line-sub { font-size: 17px; margin-top: 8px; letter-spacing: 1.4em; }

  .person { position: absolute; left: 23px; top: 148px; }
  .person__name { color: var(--sky); font-size: 20px; font-weight: 700; line-height: 1.2; }
  .person__title { color: var(--white); font-size: 14px; margin-top: 2px; }

  .contacts {
    position: absolute;
    left: 21px;
    top: 217px;
    list-style: none;
    color: var(--white);
    font-size: 14px;
    line-height: 20px;
  }
  .contacts li { display: flex; align-items: center; gap: 6px; }
  .contacts svg { width: 11px; height: 11px; flex: none; fill: var(--sky); }

  .address {
    position: absolute;
    right: 21px;
    top: 238px;
    color: var(--white);
    font-size: 14px;
    line-height: 20px;
    text-align: right;
    font-style: normal;
  }
</style>
</head>
<body>

<section class="card card--front" aria-label="Business card front">
  <div class="front__panel"></div>

  <div class="brand">
    <div class="brand__square"></div>
    <div class="brand__name">
      <span class="brand__line-main">Kelmora</span>
      <span class="brand__line-sub">Consulting</span>
    </div>
  </div>

  <div class="person">
    <p class="person__name">OWEN HARTLEY</p>
    <p class="person__title">Managing Director</p>
  </div>

  <ul class="contacts">
    <li>
      <svg viewBox="0 0 24 24"><path d="M6.6 10.8a15.1 15.1 0 0 0 6.6 6.6l2.2-2.2c.3-.3.7-.4 1-.2 1.1.4 2.3.6 3.6.6.6 0 1 .4 1 1V20c0 .6-.4 1-1 1C10.6 21 3 13.4 3 4c0-.6.4-1 1-1h3.5c.6 0 1 .4 1 1 0 1.3.2 2.5.6 3.6.1.3 0 .7-.2 1z"/></svg>
      123 456 789
    </li>
    <li>
      <svg viewBox="0 0 24 24"><path d="M2 5h20v2l-10 6L2 7zM2 9l10 6 10-6v10H2z"/></svg>
      info@kelmora.com
    </li>
    <li>
      <svg viewBox="0 0 24 24"><circle cx="12" cy="12" r="10"/></svg>
      www.kelmora.com
    </li>
  </ul>

  <address class="address">Your address, City<br>State, Zip 1234</address>
</section>

<section class="card card--back" aria-label="Business card back">
  <div class="brand">
    <div class="brand__square"></div>
    <div class="brand__name">
      <span class="brand__line-main">Kelmora</span>
      <span class="brand__line-sub">Consulting</span>
    </div>
  </div>
</section>

</body>
</html>
```